Business Card Design Project

We currently have existing logo. Looking to have nice colorful business cards done.
We would like the name of business, phone, address, email and website

Target Market(s)

25-50

Industry/Entity Type

Business

Requirements
Must have
• We are currently using
Samrakan font for our business name
Rage italic font for tag line..
you may visit our website at www.velmorita.com to get good feel

velmorita means colors in India. google velmorita to get more info

```html
<!DOCTYPE html>
<html lang="en">
<head>
<meta charset="utf-8">
<title>Velmorita Business Card</title>
<link rel="stylesheet" href="https://fonts.googleapis.com/css2?family=Questrial&family=Yellowtail&display=swap">
<style>
  :root {
    --page-bg: #ffffff;
    --card-bg: #721c2c;
    --ornament: #8f2838;
    --ink: #ffffff;
  }
  * { margin: 0; padding: 0; box-sizing: border-box; }
  html, body {
    width: 1200px;
    height: 909px;
    overflow: hidden;
    background: var(--page-bg);
  }
  .canvas {
    position: relative;
    width: 1200px;
    height: 909px;
  }
  .business-card {
    position: absolute;
    left: 169px;
    top: 217px;
    width: 879px;
    height: 500px;
    background: var(--card-bg);
    overflow: hidden;
    font-family: "Questrial", sans-serif;
    color: var(--ink);
  }
  .floral-flourish {
    position: absolute;
    left: 3px;
    top: 105px;
    width: 876px;
    height: 310px;
    border-radius: 50%;
    background: radial-gradient(ellipse at 60% 50%, var(--ornament) 0%, rgba(143, 40, 56, 0.55) 45%, rgba(143, 40, 56, 0) 75%);
  }
  .contact-lines {
    position: absolute;
    left: 41px;
    top: 46px;
    font-size: 28px;
    line-height: 40px;
    letter-spacing: 2.4px;
  }
  .brand-name {
    position: absolute;
    left: 247px;
    top: 222px;
    width: 330px;
    text-align: center;
    font-size: 74px;
    line-height: 1;
    letter-spacing: 2px;
  }
  .brand-tagline {
    position: absolute;
    left: 491px;
    top: 306px;
    font-family: "Yellowtail", cursive;
    font-size: 42px;
    line-height: 1.1;
    letter-spacing: 0.5px;
  }
  .address {
    position: absolute;
    left: 0;
    top: 436px;
    width: 879px;
    text-align: center;
    font-size: 28px;
    letter-spacing: 3px;
  }
</style>
</head>
<body>
<main class="canvas">
  <section class="business-card">
    <div class="floral-flourish" role="img" aria-label="Decorative swirling floral flourish in a lighter maroon tone"></div>
    <div class="contact-lines">
      <p class="contact-email">E. info@velmorita.com</p>
      <p class="contact-phone">P. 408.555.0142</p>
    </div>
    <p class="brand-name">velmorita</p>
    <p class="brand-tagline">India Restaurant</p>
    <p class="address">1480 Linden Avenue , San Jose, CA</p>
  </section>
</main>
</body>
</html>
```